Simple, bright, clean website - 3 pages, easy to update with WordPress!

I want to update my website (brevatlo.com) with a brighter/cleaner interface. It is quite dark right now. I would like it to be similar to a partner site (https://www.velmo-482.com/). White with some orange highlights (matching the logo). I want to be able to easily update the site content. There should be 3 main pages: About, Services, Contact. I also like a design similar to tarnop.com

Target Market(s)

Anyone using technology to achieve business goals.

Industry/Entity Type

Managed Service Provider (IT)

Coding

Coded - Design and coding required

Number of Pages Required

3 page

Colors
F0912C
F2A743
F7CA91
FBE8D2
FDF5EE

Requirements
Must have
• Links to standard social media apps like LinkedIn, Facebook, etc.. Easy to edit and add pages.

```html
<!DOCTYPE html>
<html lang="en">
<head>
<meta charset="utf-8">
<title>Brevatlo – Contact Us</title>
<link href="https://fonts.googleapis.com/css2?family=Poppins:wght@300;400;500;600;700&display=swap" rel="stylesheet">
<style>
:root{
  --orange:#f9ab17;
  --orange-deep:#f0912c;
  --cream:#fdf8f1;
  --ink:#222;
  --grey:#555;
  --light-grey:#9a9a9a;
  --dark:#4a4a4a;
  --white:#fff;
}
*{margin:0;padding:0;box-sizing:border-box}
html,body{width:1200px;height:2188px;overflow:hidden}
body{position:relative;font-family:'Poppins',sans-serif;background:var(--white);color:var(--ink)}
.abs{position:absolute}
.brand{font-family:'Poppins',sans-serif;font-weight:300;color:#8f8f8f;font-size:56px;letter-spacing:1px;left:88px;top:44px;line-height:1}
.badge{left:407px;top:14px;width:112px;height:112px;border-radius:50%;background:#101c1c}
.btn-pill{border-radius:24px;color:var(--white);font-weight:600;font-size:15px;display:flex;align-items:center;justify-content:center;gap:8px;height:40px;top:34px}
.btn-login{left:719px;width:178px;background:var(--dark)}
.btn-tech{left:909px;width:207px;background:var(--orange)}
.main-nav a{position:absolute;top:91px;font-size:15px;color:#333;text-decoration:none}
.main-nav a.current{color:var(--orange)}
.nav-underline{left:1011px;top:116px;width:114px;height:2px;background:var(--orange)}
.hero{left:0;top:139px;width:1200px;height:721px;background:linear-gradient(180deg,#3f6f9e 0%,#6a95b8 45%,#8ea7b4 62%,#6c7a78 82%,#4d5a34 100%)}
.hero-title{left:0;top:326px;width:1200px;text-align:center;color:var(--white);font-weight:700;font-size:69px;line-height:87px;text-shadow:3px 3px 0 #111}
.hero-btn{left:490px;top:529px;width:220px;height:61px;border-radius:31px;background:var(--orange);color:var(--white);font-weight:600;font-size:18px;display:flex;align-items:center;justify-content:center}
.dots{left:563px;top:782px;display:flex;gap:6px}
.dots span{width:14px;height:14px;border-radius:50%;background:rgba(255,255,255,.35)}
.dots span:first-child{background:var(--white)}
.section-title{left:0;top:950px;width:1200px;text-align:center;color:var(--orange);font-weight:500;font-size:52px;line-height:62px}
.section-sub{left:0;top:1004px;width:1200px;text-align:center;color:#8a8a8a;font-size:26px;letter-spacing:4px}
.intro{left:220px;top:1068px;width:760px;text-align:center;font-size:15.5px;line-height:26px;color:#333}
.form-rule{left:99px;top:1165px;width:1005px;height:7px;background:var(--orange)}
.form-panel{left:87px;top:1172px;width:1027px;height:571px;background:var(--cream)}
.field{background:var(--white);box-shadow:0 1px 4px rgba(0,0,0,.08);color:#888;font-size:15px;padding-left:24px;display:flex;align-items:center}
.field.msg{align-items:flex-start;padding-top:24px}
.submit{left:172px;top:1606px;width:192px;height:59px;border-radius:30px;background:var(--orange);color:var(--white);font-weight:600;font-size:20px;display:flex;align-items:center;justify-content:center}
.info-icon{width:35px;height:35px;background:var(--orange);border-radius:3px;display:flex;align-items:center;justify-content:center}
.info-label{color:var(--orange);font-size:18px;font-weight:500;line-height:22px}
.info-value{font-size:17px;line-height:22px;color:#111}
.footer{left:0;top:1817px;width:1200px;height:307px;background:var(--orange)}
.footer-brand{left:0;top:1890px;width:1200px;text-align:center;color:var(--white);font-weight:300;font-size:84px;line-height:1}
.footer-rule{left:91px;top:2037px;width:1028px;height:1px;background:rgba(255,255,255,.5)}
.footer-nav{left:0;top:2059px;width:1200px;display:flex;justify-content:center;gap:35px;color:var(--white);font-size:15px}
.bottom-bar{left:0;top:2124px;width:1200px;height:64px;background:var(--dark)}
.copyright{left:89px;top:2148px;color:var(--white);font-size:14.5px}
.socials{left:961px;top:2141px;display:flex;gap:6px}
.socials a{width:35px;height:35px;border:1px solid var(--white);border-radius:3px;display:block}
</style>
</head>
<body>
<header>
  <div class="abs brand">brevatlo</div>
  <div class="abs badge" role="img" aria-label="Anniversary badge"></div>
  <a class="abs btn-pill btn-login">
    <svg width="16" height="16" viewBox="0 0 16 16"><circle cx="8" cy="5" r="3.5" fill="#fff"/><path d="M1.5 15c0-4 3-6 6.5-6s6.5 2 6.5 6z" fill="#fff"/></svg>CLIENT LOGIN</a>
  <a class="abs btn-pill btn-tech">
    <svg width="20" height="20" viewBox="0 0 20 20" fill="none" stroke="#fff" stroke-width="2"><rect x="2" y="9" width="9" height="5" rx="2.5" transform="rotate(-45 6.5 11.5)"/><rect x="9" y="6" width="9" height="5" rx="2.5" transform="rotate(-45 13.5 8.5)"/></svg>CONNECT MY TECH</a>
  <nav class="main-nav">
    <a style="left:712px">HOME</a>
    <a style="left:793px">ABOUT US</a>
    <a style="left:909px">SERVICES</a>
    <a class="current" style="left:1019px">CONTACT US</a>
  </nav>
  <div class="abs nav-underline"></div>
</header>

<section>
  <div class="abs hero" role="img" aria-label="City skyline photo with trees in the foreground"></div>
  <h1 class="abs hero-title">YOUR PARTNER IN TRUSTED<br>TECHNOLOGY SOLUTIONS</h1>
  <a class="abs hero-btn">CONTACT US</a>
  <div class="abs dots"><span></span><span></span><span></span><span></span></div>
</section>

<section>
  <h2 class="abs section-title">Contact Us</h2>
  <div class="abs section-sub">Get In Touch</div>
  <p class="abs intro">If you have any questions or need help, please fill out the form below. We are here to help and answer any questions you might have. We look forward to hearing from you.</p>
  <div class="abs form-rule"></div>
  <div class="abs form-panel"></div>
  <div class="abs field" style="left:171px;top:1250px;width:255px;height:53px">First Name:</div>
  <div class="abs field" style="left:449px;top:1250px;width:255px;height:53px">Last Name:</div>
  <div class="abs field" style="left:171px;top:1325px;width:255px;height:52px">Phone:</div>
  <div class="abs field" style="left:449px;top:1325px;width:255px;height:52px">Email:</div>
  <div class="abs field msg" style="left:172px;top:1401px;width:531px;height:163px">Mesage:</div>
  <a class="abs submit">SUBMIT NOW</a>

  <div class="abs info-icon" style="left:774px;top:1329px">
    <svg width="16" height="16" viewBox="0 0 16 16"><path d="M4 1l2 4-1.5 1.5a8 8 0 0 0 5 5L11 10l4 2-1 3C8 15 1 8 1 2z" fill="#fff"/></svg>
  </div>
  <div class="abs info-label" style="left:835px;top:1323px">CALL US</div>
  <div class="abs info-value" style="left:835px;top:1347px">8012 555 0147</div>
  <div class="abs info-icon" style="left:774px;top:1397px">
    <svg width="16" height="12" viewBox="0 0 16 12"><rect width="16" height="12" fill="#fff"/><path d="M0 0l8 6 8-6" stroke="#f9ab17" stroke-width="1.5" fill="none"/></svg>
  </div>
  <div class="abs info-label" style="left:835px;top:1391px">EMAIL US</div>
  <div class="abs info-value" style="left:835px;top:1414px">info@brevatlo.com</div>
</section>

<footer>
  <div class="abs footer"></div>
  <div class="abs footer-brand">brevatlo</div>
  <div class="abs footer-rule"></div>
  <nav class="abs footer-nav"><span>HOME</span><span>|</span><span>ABOUT US</span><span>|</span><span>SERVICES</span><span>|</span><span>CONTACT US</span></nav>
  <div class="abs bottom-bar"></div>
  <div class="abs copyright">Copyright © 2024 All Rights Reserved By Company name</div>
  <div class="abs socials"><a aria-label="Social link"></a><a aria-label="Social link"></a><a aria-label="Social link"></a><a aria-label="Social link"></a></div>
</footer>
</body>
</html>
```